Photography Price List DL flyer

In need of a double sided DL flyer to list prices for a photography business that is in the real estate industry. Will need to include logo and be themed to match. Price details and contact information are in the pdf attached.

Below are links to the logo and photos that can be used on the flyer.

Logo
https://www.filquarry.net/s/tmewqoral7bnzx/LogoFiles.zip?dl=0

Photos
https://www.filquarry.net/s/p3vhnkelo81rtw/Website_Images.zip?dl=0

Sorry people the photo examples I put the wrong link. I have fixed it in the brief but the proper link is: https://www.filquarry.net/s/p3vhnkelo81rtw/Website_Images.zip?dl=0

Also dimensions of a DL are 210mm x 99mm + 3m bleed. Thanks

Target Market(s)

Real estate agents

Industry/Entity Type

Business

Requirements
Must have
• Price lists and contact information

```html
<!DOCTYPE html>
<html lang="en">
<head>
<meta charset="utf-8">
<title>Brightway Photos – DL Price Flyer</title>
<link rel="stylesheet" href="https://fonts.googleapis.com/css2?family=Josefin+Sans:wght@400;600;700&display=swap">
<style>
  :root {
    --backdrop: #d8d3cb;
    --charcoal: #444545;
    --leaf: #acd27a;
    --coral: #ef6a6f;
    --paper: #ffffff;
    --ink: #2c2c2c;
    --mist: #dcdde0;
    --sky-top: #2f7de0;
    --sky-low: #9cc6f0;
    --lawn: #6fae3a;
  }
  * { box-sizing: border-box; margin: 0; padding: 0; }
  html, body {
    width: 1085px; height: 1200px; overflow: hidden;
    background: var(--backdrop);
    font-family: "Josefin Sans", sans-serif;
  }
  .flyer {
    position: absolute; top: 60px;
    width: 480px; height: 1078px;
    background: var(--paper);
    box-shadow: 0 2px 8px rgba(0,0,0,.25);
    overflow: hidden;
  }
  .flyer--front { left: 47px; }
  .flyer--back { left: 562px; }

  /* front */
  .front-header { position: absolute; top: 0; left: 0; width: 480px; height: 133px; }
  .front-header__block { position: absolute; top: 0; left: 108px; width: 372px; height: 133px; background: var(--leaf); }
  .front-photo {
    position: absolute; top: 133px; left: 0; width: 480px; height: 650px;
    background: linear-gradient(180deg, var(--sky-top) 0%, var(--sky-low) 30%, #e9e9e4 45%, #d8d6d0 70%, var(--lawn) 82%, #5f9a30 100%);
  }
  .front-footer {
    position: absolute; top: 783px; left: 0; width: 480px; height: 295px;
    background: var(--charcoal); text-align: center;
  }

  .brand {
    display: flex; align-items: center; justify-content: center; gap: 16px;
  }
  .brand__name {
    color: var(--leaf); font-weight: 600; font-size: 34px; letter-spacing: 2px;
    text-transform: uppercase; padding-top: 6px;
  }
  .brand__dot { width: 62px; height: 62px; border-radius: 50%; background: var(--coral); }

  .front-footer .brand { margin-top: 50px; }
  .contact-list { margin-top: 44px; color: var(--leaf); font-variant: small-caps; }
  .contact-list__main { font-size: 29px; letter-spacing: 1px; }
  .contact-list__line { font-size: 22px; margin-top: 12px; letter-spacing: .5px; }
  .contact-list__line--small { font-size: 20px; margin-top: 12px; }

  /* back */
  .back-photo {
    position: absolute; top: 0; left: 0; width: 480px; height: 242px;
    background: linear-gradient(180deg, #a9b8c8 0%, #c7b8a2 30%, #e9a65c 52%, #b0683a 65%, #2d2a2a 80%, #151618 100%);
  }
  .back-title {
    position: absolute; top: 24px; left: 0; width: 480px; text-align: center;
    color: var(--mist); opacity: .85; font-size: 52px; letter-spacing: 8px;
    font-variant: small-caps; font-weight: 400;
  }
  .back-brandbar {
    position: absolute; top: 242px; left: 0; width: 480px; height: 134px;
    background: var(--charcoal); display: flex; align-items: center; justify-content: center;
  }
  .price-menu { position: absolute; top: 418px; left: 85px; width: 306px; color: var(--ink); }
  .price-group { margin-bottom: 40px; }
  .price-group__title { font-size: 26px; font-weight: 600; margin-bottom: 6px; }
  .price-row {
    display: flex; align-items: baseline; font-size: 21px; font-variant: small-caps;
    height: 33px; letter-spacing: .5px;
  }
  .price-row__leader { flex: 1; border-bottom: 2px dotted var(--ink); margin: 0 2px 5px; }
  .price-note { font-size: 21px; font-variant: small-caps; letter-spacing: .5px; }
  .price-note--spaced { margin-top: 34px; margin-bottom: 0; }
  .call-bar {
    position: absolute; top: 928px; left: 0; width: 480px; height: 49px;
    background: var(--coral); color: var(--ink);
    font-size: 28px; font-style: italic; font-variant: small-caps;
    padding: 12px 0 0 84px; letter-spacing: 1px;
  }
  .back-footer {
    position: absolute; top: 977px; left: 0; width: 480px; height: 101px;
    background: var(--charcoal); color: var(--paper); padding: 18px 0 0 84px;
    font-variant: small-caps; font-size: 19px;
  }
  .back-footer p + p { margin-top: 16px; }
</style>
</head>
<body>
  <section class="flyer flyer--front">
    <div class="front-header"><div class="front-header__block"></div></div>
    <div class="front-photo" role="img" aria-label="Photograph of a white two-storey house with balcony, garage and front lawn under blue sky"></div>
    <div class="front-footer">
      <div class="brand">
        <span class="brand__name">Brightway Photos</span>
        <span class="brand__dot"></span>
      </div>
      <div class="contact-list">
        <p class="contact-list__main">Contact Us &nbsp;: 0400 555 017</p>
        <p class="contact-list__line">Log on &nbsp;: brightwayphotos.com.au</p>
        <p class="contact-list__line--small">Email : info@brightwayphotos.com.au</p>
      </div>
    </div>
  </section>

  <section class="flyer flyer--back">
    <div class="back-photo" role="img" aria-label="Photograph of a city skyline at dusk with orange sunset sky"></div>
    <h1 class="back-title">Price Menu</h1>
    <div class="back-brandbar">
      <div class="brand">
        <span class="brand__name">Brightway Photos</span>
        <span class="brand__dot"></span>
      </div>
    </div>

    <div class="price-menu">
      <div class="price-group">
        <h2 class="price-group__title">Photography</h2>
        <div class="price-row"><span>10 images</span><span class="price-row__leader"></span><span>$149</span></div>
        <div class="price-row"><span>12 - 15 images</span><span class="price-row__leader"></span><span>$179</span></div>
        <div class="price-row"><span>20+ images</span><span class="price-row__leader"></span><span>$229</span></div>
      </div>
      <div class="price-group">
        <h2 class="price-group__title">Twilight</h2>
        <p class="price-note">Add $100 to image package</p>
        <div class="price-row price-note--spaced"><span>Floorplans -</span><span class="price-row__leader"></span><span>$49</span></div>
      </div>
      <div class="price-group">
        <h2 class="price-group__title">Video</h2>
        <div class="price-row"><span>30 seconds</span><span class="price-row__leader"></span><span>$150</span></div>
        <div class="price-row"><span>60 seconds</span><span class="price-row__leader"></span><span>$200</span></div>
        <div class="price-row"><span>2 minutes</span><span class="price-row__leader"></span><span>$300</span></div>
      </div>
    </div>

    <div class="call-bar">Call us &nbsp;:0400 555 017</div>
    <div class="back-footer">
      <p>W : brightwayphotos.com.au</p>
      <p>E : info@brightwayphotos.com.au</p>
    </div>
  </section>
</body>
</html>
```